Colin Dwyer Moving DL Flyer

We need a double sided DL flyer to give to patients to let them know that we are moving location.
On one side we would like it to read:
"We Are Moving!" and "November 2017" and our logo.
On the other side we would like it to read:
"Same Great Staff"
"Same Great Service"
"Bigger, Brighter and Better"
"New Location at 52 Fernlow St"
with a map below (attached)
The flyer should follow our practice branding. Attached is a copy of our business card as an example of this.

```html
<!DOCTYPE html>
<html lang="en">
<head>
<meta charset="utf-8">
<title>Colin Dwyer Optometry – Moving DL Flyer</title>
<link rel="stylesheet" href="https://fonts.googleapis.com/css2?family=Roboto:wght@300;400;500;700;900&display=swap">
<style>
  :root {
    --backdrop: #d1d2d4;
    --plum: #523c56;
    --plum-light: #6a4f86;
    --plum-soft: #5f4864;
    --white: #ffffff;
    --ink: #2e2a30;
    --map-grey: #c7c7c9;
  }
  * { box-sizing: border-box; margin: 0; padding: 0; }
  html, body { width: 1200px; height: 1200px; overflow: hidden; }
  body {
    background: var(--backdrop);
    font-family: "Roboto", Arial, sans-serif;
    position: relative;
  }
  .flyer {
    position: absolute;
    top: 120px;
    width: 463px;
    height: 960px;
    overflow: hidden;
  }
  .flyer--front { left: 86px; background: var(--white); }
  .flyer--back { left: 614px; background: var(--plum); color: var(--white); }

  .brand {
    position: absolute;
    top: 68px;
    left: 0;
    width: 100%;
    text-align: center;
    font-weight: 500;
    line-height: 1;
  }
  .brand__name { display: block; font-size: 30px; }
  .brand__trade { display: block; font-size: 46px; margin-top: 4px; }
  .flyer--front .brand { color: var(--plum); }
  .flyer--back .brand { color: var(--white); }

  .badge {
    position: absolute;
    left: 0; top: 0;
    width: 463px; height: 720px;
  }
  .headline {
    position: absolute;
    left: 0; width: 100%;
    text-align: center;
    color: var(--white);
  }
  .headline__main {
    top: 325px;
    font-weight: 900;
    font-size: 76px;
    line-height: 0.98;
    letter-spacing: -1px;
    transform: rotate(-4deg);
    text-shadow: 3px 3px 0 var(--plum-light);
  }
  .headline__date {
    top: 500px;
    font-weight: 300;
    font-size: 58px;
    line-height: 1.08;
    transform: rotate(-4deg);
  }
  .tagline {
    position: absolute;
    left: 162px;
    top: 816px;
    font-size: 30px;
    font-weight: 400;
    color: var(--ink);
  }
  .web {
    position: absolute;
    left: 167px;
    top: 873px;
    font-size: 20px;
    font-weight: 300;
    color: var(--plum);
  }

  .promises { position: absolute; left: 67px; top: 211px; list-style: none; }
  .promise {
    display: flex; align-items: center;
    height: 60px; margin-bottom: 14px;
  }
  .promise__icon {
    width: 60px; height: 60px; border-radius: 50%;
    background: #ecebee;
    display: flex; align-items: center; justify-content: center;
    margin-right: 17px;
  }
  .promise__text { font-size: 19px; letter-spacing: 1px; font-weight: 400; }

  .location {
    position: absolute; top: 456px; left: 0; width: 100%;
    text-align: center;
  }
  .location__label { display: block; font-size: 18px; font-weight: 300; margin-top: 6px; }
  .location__address { display: block; font-size: 31px; font-weight: 700; margin-top: 4px; }

  .map-area { position: absolute; left: 0; top: 555px; width: 463px; height: 405px; }
</style>
</head>
<body>

  <section class="flyer flyer--front" aria-label="Front of flyer">
    <svg class="badge" viewBox="0 0 463 720" aria-hidden="true">
      <circle cx="238" cy="450" r="262" fill="var(--plum-light)"/>
      <circle cx="230" cy="445" r="262" fill="var(--plum)"/>
    </svg>
    <div class="brand">
      <span class="brand__name">Colin Dwyer</span>
      <span class="brand__trade">Optometry</span>
    </div>
    <h1 class="headline headline__main">WE ARE<br>MOVING!</h1>
    <p class="headline headline__date">NOVEMBER<br>2017</p>
    <p class="tagline">See Better. See Us.</p>
    <p class="web">www.colindwyer.com.au</p>
  </section>

  <section class="flyer flyer--back" aria-label="Back of flyer">
    <div class="brand">
      <span class="brand__name">Colin Dwyer</span>
      <span class="brand__trade">Optometry</span>
    </div>

    <ul class="promises">
      <li class="promise">
        <span class="promise__icon">
          <svg width="30" height="30" viewBox="0 0 30 30" aria-hidden="true">
            <path d="M6 15 l6 6 l12 -13" fill="none" stroke="var(--plum)" stroke-width="4" stroke-linecap="round" stroke-linejoin="round"/>
          </svg>
        </span>
        <span class="promise__text">Same Great Staff</span>
      </li>
      <li class="promise">
        <span class="promise__icon">
          <svg width="32" height="30" viewBox="0 0 32 30" aria-hidden="true">
            <path d="M4 4 h24 a2 2 0 0 1 2 2 v13 a2 2 0 0 1 -2 2 h-14 l-7 6 v-6 h-3 a2 2 0 0 1 -2 -2 v-13 a2 2 0 0 1 2 -2z" fill="var(--plum)"/>
          </svg>
        </span>
        <span class="promise__text">Same Great Service</span>
      </li>
      <li class="promise">
        <span class="promise__icon">
          <svg width="30" height="30" viewBox="0 0 30 30" aria-hidden="true">
            <path d="M15 3 l3.6 7.4 8.1 1.1 -5.9 5.7 1.4 8 -7.2 -3.8 -7.2 3.8 1.4 -8 -5.9 -5.7 8.1 -1.1z" fill="var(--plum)"/>
          </svg>
        </span>
        <span class="promise__text">Bigger, Brighter and Better</span>
      </li>
    </ul>

    <div class="location">
      <svg width="22" height="30" viewBox="0 0 22 30" aria-hidden="true">
        <path d="M11 1 a10 10 0 0 1 10 10 c0 7 -10 18 -10 18 s-10 -11 -10 -18 a10 10 0 0 1 10 -10z" fill="var(--white)"/>
        <circle cx="11" cy="11" r="4" fill="var(--plum)"/>
      </svg>
      <span class="location__label">New Location at</span>
      <span class="location__address">52 Fernlow St</span>
    </div>

    <svg class="map-area" viewBox="0 0 463 405" role="img" aria-label="Street map showing the new practice location, surrounding roads, car parking and the neighbouring marketplace">
      <path d="M0 125 Q231.5 -30 463 125 V405 H0z" fill="var(--white)"/>
      <path d="M0 140 Q231.5 -4 463 140 V405 H0z" fill="var(--map-grey)"/>
    </svg>
  </section>

</body>
</html>
```